dsadasdasdasdsa

Industry/Entity Type

Mortgage Broking

Requirements
Must have
• Call-to-action button somewhere on the graphic
Nice to have
• The font of our logo is Montserrat

```html
<!DOCTYPE html>
<html lang="en">
<head>
<meta charset="utf-8">
<title>Need a Mortgage Broker? Banner</title>
<link href="https://fonts.googleapis.com/css2?family=Montserrat:wght@400;500;600&display=swap" rel="stylesheet">
<style>
  :root {
    --stage: #383838;
    --paper-center: #fbfdf7;
    --paper-edge: #e6f3da;
    --swoosh-dark: #00a94f;
    --swoosh-mid: #3dbb3a;
    --swoosh-light: #a6d63a;
    --headline: #6b1a10;
    --cta-dark: #009448;
    --cta-light: #8cc63f;
    --cta-text: #ffffff;
    --mascot-shell: #9a5a2e;
    --mascot-skin: #5cbf57;
  }
  * { box-sizing: border-box; margin: 0; padding: 0; }
  html, body {
    width: 1200px; height: 1200px; overflow: hidden;
    background: var(--stage);
  }
  .banner {
    position: absolute;
    left: 53px; top: 525px;
    width: 1093px; height: 150px;
    background: radial-gradient(ellipse 60% 120% at 50% 55%, var(--paper-center) 0%, var(--paper-edge) 100%);
    box-shadow: 0 6px 18px rgba(0,0,0,0.55);
    overflow: hidden;
    font-family: "Montserrat", sans-serif;
  }
  .swoosh { position: absolute; top: 0; height: 150px; }
  .swoosh--left { left: 0; width: 160px; }
  .swoosh--right { right: 0; width: 170px; }
  .mascot {
    position: absolute; top: 3px; height: 147px;
    border-radius: 45% 45% 20% 20%;
    background: linear-gradient(160deg, var(--mascot-skin) 0%, var(--mascot-shell) 55%, var(--mascot-skin) 100%);
    opacity: 0.85;
  }
  .mascot--left { left: 127px; width: 106px; }
  .mascot--right { left: 876px; width: 96px; }
  .headline {
    position: absolute; left: 0; right: 0; top: 30px;
    text-align: center;
    font-weight: 600; font-size: 36px; line-height: 44px;
    color: var(--headline);
    letter-spacing: 0.2px;
  }
  .cta {
    position: absolute; left: 320px; top: 84px;
    width: 465px; height: 29px;
    border-radius: 4px;
    background: linear-gradient(90deg, var(--cta-dark) 0%, var(--cta-light) 50%, var(--cta-dark) 100%);
    color: var(--cta-text);
    font-weight: 500; font-size: 19.5px; line-height: 29px;
    text-align: center;
    text-decoration: none;
  }
</style>
</head>
<body>
  <div class="banner">
    <svg class="swoosh swoosh--left" viewBox="0 0 160 150" preserveAspectRatio="none" aria-hidden="true">
      <defs>
        <linearGradient id="swooshLeftFill" x1="0" y1="0" x2="1" y2="1">
          <stop offset="0" stop-color="var(--swoosh-dark)"/>
          <stop offset="0.5" stop-color="var(--swoosh-light)"/>
          <stop offset="1" stop-color="var(--swoosh-mid)"/>
        </linearGradient>
      </defs>
      <path d="M0 0 H34 C40 60 80 120 150 150 H0 Z" fill="url(#swooshLeftFill)"/>
      <path d="M16 0 C24 70 70 125 135 150" stroke="#ffffff" stroke-opacity="0.35" stroke-width="1.5" fill="none"/>
    </svg>

    <div class="mascot mascot--left" role="img" aria-label="Cartoon turtle mascot waving with an open hand"></div>

    <h1 class="headline">Need a Mortgage Broker?</h1>
    <a class="cta" href="#">Search Now on Australia's Largest Directory</a>

    <div class="mascot mascot--right" role="img" aria-label="Cartoon turtle mascot pointing toward the headline"></div>

    <svg class="swoosh swoosh--right" viewBox="0 0 170 150" preserveAspectRatio="none" aria-hidden="true">
      <defs>
        <linearGradient id="swooshRightFill" x1="0" y1="0" x2="1" y2="1">
          <stop offset="0" stop-color="var(--swoosh-mid)"/>
          <stop offset="0.5" stop-color="var(--swoosh-light)"/>
          <stop offset="1" stop-color="var(--swoosh-dark)"/>
        </linearGradient>
      </defs>
      <path d="M0 0 H170 V150 H120 C110 80 80 30 0 0 Z" fill="url(#swooshRightFill)"/>
      <path d="M20 0 C100 25 135 80 145 150" stroke="#ffffff" stroke-opacity="0.35" stroke-width="1.5" fill="none"/>
    </svg>
  </div>
</body>
</html>
```